Produktbroschüre
Zielgruppe
Einzelhändler im Einrichtungs-, Geschenk- und Blumanfachhandel, Dekorateure, Innenarchitekten,
Aufgabenstellung
Ich bin Existenzgründer und brauche eine ansprechende Produktbroschüre für Inneneinrichtungsdeko und Accessoires.
Die Artikel wechseln öfter und ich möchte in der Lage sein Bilder und Texte einfach auszutauschen. Über die zeit, wird das Sortiment erwetert, die Broschüre sollte einfach mitwachsen können.
Momentan behelfe ich mir mit Scribus und Gimp für Windows, bin aber kein Experte.
Als Anhang meine momentane, selbst gebaute Broschüre.

```html
<!DOCTYPE html>
<html lang="de">
<head>
<meta charset="utf-8">
<title>sorel bunt – Produktbroschüre</title>
<link href="https://fonts.googleapis.com/css2?family=Open+Sans:ital,wght@0,400;0,700;0,800;1,400;1,700;1,800&display=swap" rel="stylesheet">
<style>
  :root {
    --ink: #231f20;
    --ghost: #3b3738;
    --orange: #f08a00;
    --paper: #ffffff;
    --stage: #d8d5d0;
    --muted: #b9b4b0;
    --text-dark: #333;
  }
  * { box-sizing: border-box; margin: 0; padding: 0; }
  html, body { width: 1200px; height: 848px; overflow: hidden; }
  body { background: var(--stage); font-family: "Open Sans", Arial, sans-serif; position: relative; }

  .spread { position: absolute; width: 510px; height: 260px; box-shadow: 0 2px 6px rgba(0,0,0,.35); }
  .spread::after { content: ""; position: absolute; left: 254px; top: 0; width: 2px; height: 100%; background: rgba(0,0,0,.45); }
  .page { position: absolute; top: 0; width: 255px; height: 260px; background: var(--ink); overflow: hidden; }
  .page.left { left: 0; }
  .page.right { left: 255px; }

  .ghost { position: absolute; top: 14px; font-weight: 800; font-size: 34px; color: var(--ghost); letter-spacing: .5px; white-space: nowrap; }
  .left .ghost { left: 22px; }
  .right .ghost { left: -50px; }
  .run-head { position: absolute; top: 10px; font-style: italic; font-weight: 700; font-size: 7.5px; color: #fff; white-space: nowrap; z-index: 1; }
  .left .run-head { left: 34px; }
  .right .run-head { left: 54px; }
  .folio { position: absolute; bottom: 8px; font-size: 5px; color: var(--muted); }
  .left .folio { left: 12px; }
  .right .folio { right: 12px; }

  .panel { position: absolute; left: 12px; top: 54px; width: 222px; height: 150px; background: var(--paper); border: 2px solid var(--orange); border-radius: 8px; overflow: hidden; }
  .left .panel.photo-panel { left: 24px; }
  .photo { position: absolute; inset: 10px 14px 10px 14px; border-radius: 4px; }

  .caption { position: absolute; top: 196px; width: 92px; min-height: 34px; padding: 4px 4px; background: var(--orange); border-radius: 4px; color: #fff; text-align: center; z-index: 2; }
  .caption h3 { font-style: italic; font-weight: 700; font-size: 9.5px; line-height: 1.2; }
  .caption p { font-style: italic; font-size: 5px; line-height: 1.3; }
  .note { position: absolute; top: 208px; width: 110px; font-size: 4.6px; line-height: 1.35; color: var(--muted); }

  .tab { position: absolute; top: 92px; width: 18px; height: 74px; background: var(--orange); color: #fff; font-style: italic; font-weight: 700; font-size: 8px; display: flex; align-items: center; justify-content: center; writing-mode: vertical-rl; white-space: nowrap; }
  .tab.on-right { right: 0; border-radius: 5px 0 0 5px; transform: rotate(180deg); border-radius: 0 5px 5px 0; }
  .tab.on-left { left: 0; border-radius: 0 5px 5px 0; }

  .chapter-band { position: absolute; top: 88px; height: 30px; background: var(--orange); border-radius: 4px; color: #fff; font-style: italic; font-weight: 700; font-size: 17px; display: flex; align-items: center; justify-content: center; white-space: nowrap; }
  .chapter-sub { position: absolute; top: 128px; left: 20px; font-style: italic; font-size: 5.5px; color: var(--text-dark); }

  /* cover */
  .url-band { position: absolute; left: 0; top: 190px; width: 222px; height: 38px; background: var(--orange); border-radius: 0 5px 5px 0; color: #fff; font-weight: 700; font-size: 14px; display: flex; align-items: center; padding-left: 14px; }
  .cover-panel { top: 28px; height: 150px; }
  .season { position: absolute; top: 10px; right: 14px; font-size: 5px; color: var(--muted); }
  .title-box { position: absolute; left: 32px; top: 146px; width: 210px; height: 50px; background: var(--orange); border-radius: 4px; color: #fff; text-align: center; padding-top: 6px; z-index: 2; }
  .title-box p { font-style: italic; font-size: 6px; }
  .title-box h1 { font-style: italic; font-weight: 800; font-size: 23px; line-height: 1.3; }
  .cover-url { position: absolute; left: 0; right: 0; top: 214px; text-align: center; font-size: 6px; color: var(--muted); }

  /* contact + contents */
  .contact { position: absolute; left: 30px; top: 48px; width: 215px; height: 150px; background: var(--paper); border: 2px solid var(--orange); border-radius: 8px; text-align: center; padding-top: 40px; color: var(--text-dark); }
  .contact h2 { font-style: italic; font-weight: 700; font-size: 8px; margin-bottom: 4px; }
  .contact address { font-style: normal; font-size: 4.6px; line-height: 1.4; }
  .contact .web { font-weight: 700; font-size: 8px; margin-top: 10px; }
  .contents { position: absolute; left: 14px; top: 48px; width: 210px; height: 150px; background: var(--paper); border: 2px solid var(--orange); border-radius: 8px; padding: 22px 14px; }
  .contents table { border-collapse: collapse; font-size: 6px; color: var(--text-dark); }
  .contents td { padding: 1.5px 6px 1.5px 0; }
  .contents td:first-child { width: 100px; }
</style>
</head>
<body>

<!-- Spread 1: Titel -->
<section class="spread" style="left:87px; top:15px;">
  <div class="page left">
    <span class="ghost">sorel bunt</span>
    <div class="url-band">www.sorel-bunt.com</div>
  </div>
  <div class="page right">
    <span class="season">Sommer/Herbst 2009</span>
    <span class="run-head" style="top:24px; left:60px;">Exklusiv in Deutschland bei sorel bunt</span>
    <div class="panel cover-panel" style="top:36px;">
      <div class="photo" role="img" aria-label="Zwei glänzende Edelstahlschalen mit Obst" style="background:radial-gradient(ellipse at 55% 45%, #f4f4f4, #9a9a9a 60%, #e8e8e8);"></div>
    </div>
    <div class="title-box">
      <p>Wohn- und Tischkultur, Lifestyle, Gartendeko</p>
      <h1>sorel bunt</h1>
    </div>
    <div class="cover-url">www.sorel-bunt.com</div>
  </div>
</section>

<!-- Spread 2: Kontakt und Inhalt -->
<section class="spread" style="left:620px; top:15px;">
  <div class="page left">
    <span class="ghost">sorel bunt</span>
    <span class="run-head">Exklusiv in Deutschland bei sorel bunt</span>
    <div class="contact">
      <h2>sorel bunt</h2>
      <address>Inh. M. Weber<br>Lindenweg 4<br>12345 Musterstadt<br><br>info@sorel-bunt.de<br>Tel. 0123 456789</address>
      <p class="web">www.sorel-bunt.com</p>
    </div>
  </div>
  <div class="page right">
    <span class="ghost">sorel bunt</span>
    <span class="run-head">Wohn- und Tischkultur, Lifestyle, Gartendeko</span>
    <div class="contents">
      <table>
        <tr><td>01 Schalen</td><td>Seite</td><td>5–12</td></tr>
        <tr><td>02 Teelichthalter</td><td>Seite</td><td>13–18</td></tr>
        <tr><td>03 Fröhliche Tierwelt</td><td>Seite</td><td>19–24</td></tr>
        <tr><td>04 Bänke und Hocker</td><td>Seite</td><td>24</td></tr>
        <tr><td>05 Rosenfeuerwerk</td><td>Seite</td><td>25</td></tr>
      </table>
    </div>
    <div class="tab on-right">Inhalt</div>
    <span class="folio">4</span>
  </div>
</section>

<!-- Spread 3: Kapitel Schalen -->
<section class="spread" style="left:87px; top:292px;">
  <div class="page left">
    <span class="ghost">sorel bunt</span>
    <span class="run-head">Exklusiv in Deutschland bei sorel bunt</span>
    <div class="panel" style="left:14px;"></div>
    <div class="chapter-band" style="left:0; width:200px;">01 Schalen</div>
    <p class="chapter-sub">Eine wundervolle Kollektion unterschiedlicher Schalen</p>
    <span class="folio">5</span>
  </div>
  <div class="page right">
    <span class="ghost">sorel bunt</span>
    <span class="run-head">Wohn- und Tischkultur, Lifestyle, Gartendeko</span>
    <div class="panel">
      <div class="photo" role="img" aria-label="Bauchige Edelstahlschale mit Obst" style="background:radial-gradient(ellipse at 50% 50%, #f6f6f6, #a5a5a5 55%, #eaeaea);"></div>
    </div>
    <div class="tab on-right">Schalen</div>
    <div class="caption" style="left:14px;"><h3>Bauchige Schale</h3><p>doppelwandig<br>26 cm</p></div>
    <p class="note" style="left:112px;">Der Edelstahlkörper glänzt und hält Speisen lange frisch</p>
    <span class="folio">6</span>
  </div>
</section>

<!-- Spread 4: Schalen -->
<section class="spread" style="left:620px; top:292px;">
  <div class="page left">
    <span class="ghost">sorel bunt</span>
    <span class="run-head">Exklusiv in Deutschland bei sorel bunt</span>
    <div class="panel photo-panel">
      <div class="photo" role="img" aria-label="Doppelwandschalen aus Edelstahl in vier Größen mit Beeren" style="background:radial-gradient(ellipse at 45% 55%, #f2f2f2, #a0a0a0 55%, #f5f5f5);"></div>
    </div>
    <div class="tab on-left">Schalen</div>
    <p class="note" style="left:14px; width:100px;">Zum Servieren von Obst, Salat und Snacks</p>
    <div class="caption" style="left:130px;"><h3>Doppelwandschale</h3><p>doppelwandig<br>14, 20, 24 und 28 cm</p></div>
    <span class="folio">7</span>
  </div>
  <div class="page right">
    <span class="ghost">sorel bunt</span>
    <span class="run-head">Wohn- und Tischkultur, Lifestyle, Gartendeko</span>
    <div class="panel">
      <div class="photo" role="img" aria-label="Flache Aluminiumschale auf hellem Grund" style="background:radial-gradient(ellipse at 50% 50%, #8d9396, #c4c8ca 55%, #f4f4f4);"></div>
    </div>
    <div class="tab on-right">Schalen</div>
    <div class="caption" style="left:14px;"><h3>Fallenschale</h3><p>70 cm/90 cm</p></div>
    <p class="note" style="left:112px;">Zum Dekorieren, wetterfest</p>
    <span class="folio">8</span>
  </div>
</section>

<!-- Spread 5: Teelichthalter -->
<section class="spread" style="left:87px; top:567px;">
  <div class="page left">
    <span class="ghost">sorel bunt</span>
    <span class="run-head">Exklusiv in Deutschland bei sorel bunt</span>
    <div class="panel photo-panel">
      <div class="photo" role="img" aria-label="Teelichthalter aus Glas mit dunklem Sockel" style="background:radial-gradient(ellipse at 50% 55%, #c9c9c9, #f3f3f3 55%, #ffffff);"></div>
    </div>
    <div class="tab on-left">Teelichthalter</div>
    <p class="note" style="left:24px; width:100px;">Teelichthalter aus mundgeblasenem Glas mit Sockel</p>
    <div class="caption" style="left:140px;"><h3>Brunnen</h3><p>aus Glas<br>12 x 14 cm</p></div>
    <span class="folio">13</span>
  </div>
  <div class="page right">
    <span class="ghost">sorel bunt</span>
    <span class="run-head">Wohn- und Tischkultur, Lifestyle, Gartendeko</span>
    <div class="panel">
      <div class="photo" role="img" aria-label="Bunte hängende Glas-Teelichter in Rot, Türkis, Grün und Pink" style="background:linear-gradient(90deg, #f6d2c4 0%, #fff 30%, #cfe9ea 50%, #e3f0c6 70%, #f4cfe0 100%);"></div>
    </div>
    <div class="tab on-right">Teelichthalter</div>
    <div class="caption" style="left:14px;"><h3>Webernest</h3><p>Glas, bunt<br>20 cm</p></div>
    <p class="note" style="left:112px;">Hängende Teelichter in vier Farben</p>
    <span class="folio">14</span>
  </div>
</section>

<!-- Spread 6: Fröhliche Tierwelt -->
<section class="spread" style="left:620px; top:567px;">
  <div class="page left">
    <span class="ghost">sorel bunt</span>
    <span class="run-head">Exklusiv in Deutschland bei sorel bunt</span>
    <div class="panel" style="left:14px;"></div>
    <div class="chapter-band" style="left:2px; width:210px;">03 Föhliche Tierwelt</div>
    <span class="folio">19</span>
  </div>
  <div class="page right">
    <span class="ghost">sorel bunt</span>
    <span class="run-head">Wohn- und Tischkultur, Lifestyle, Gartendeko</span>
    <div class="panel">
      <div class="photo" role="img" aria-label="Rostige Metallvögel auf Stielen: Kranich, Reiher und Ente" style="background:linear-gradient(90deg, #fff 0%, #e7ddd5 30%, #fff 55%, #e5d9cf 80%, #fff 100%);"></div>
      <span style="position:absolute; left:22px; bottom:18px; font-size:4.5px; color:#555;">Kranich</span>
      <span style="position:absolute; left:92px; bottom:40px; font-size:4.5px; color:#555;">Reiher</span>
      <span style="position:absolute; left:160px; bottom:22px; font-size:4.5px; color:#555;">Ente</span>
    </div>
    <div class="tab on-right">Fröhliche Tierwelt</div>
    <div class="caption" style="left:96px; top:200px;"><h3>Vögel am Stiel</h3></div>
    <p class="note" style="left:190px; width:50px; top:200px;">Metallvögel auf Stiel für Garten und Topf</p>
    <span class="folio">20</span>
  </div>
</section>

</body>
</html>
```